Simple and clean poster/flyer design needed for public speaker!

SIMPLE AND CLEAN DESIGN NEEDED FOR POSTER/FLYER

I AM a public speaker based in London (www.tobiaskernwald.com)
and I would like to have a custom-made flyer/poster
(preferably in adobe CS4 template format) that I con customize (just changing the text) for my various speeches, topics and locations

I am looking for something very simple and clean.
NO extravagance or crowded poster, but a rather beautiful clean and eye-catching design that clearly informs people what i am talking about, where and when.

Go to my website www.tobiaskernwald.com
to see the colour scheme and style that I like
my poster should be like the website, similar colours, logo, clean, simple and clear.

Summary

(1) simple and clean design
(2) design that fits my brand (see website)
(3) clear and eye-catching to promote my speeches
(4) customizable for my various talks, by simply chancing the text (Please Adobe Photoshop CS4 template format)
(5)in A3, A4, A5, A6 sizes, so i can use it for both flyers and small posters

ADDITIONS

BIG BOLD HEADLINE TO GRAP ATTENTION, greatest prominence

sub headline to explain, smaller than the headline, but still prominent on the poster

just a few bullet points to list the benefits and answer the “whats in for me”-question
this is for people who are already interested and continue reading, medium prominence.

WHERE, WHEN, HOW MUCH-information, in the lower section of the poster, little text, but clearly visible

only one point of CONTACT on my poster “www.tobiaskernwald.com”, bit big and clear so that it is very prominent

little text, effectively used
LESS IS MORE
Updates

contact me regarding logo files and any questions you may have!

for the logo files go to

https://secure.dropvaultly.com/fs/v.aspx?v=41958b2d703c9ea1f6d2

click on the folder "logo pack" to see the files

eps
jpg
png
photoshop
TIF

thanks for your interest. hope to see great designs!
I am really looking forward to it
if you have any questions, please do not hesitate to ask

Kind Regards
Tobias
 

• Simple, clean design, text sparingly used.

• The mood should be light-hearted, calm, bright, simple and friendly, comic like

• a lot of white space, calling more attention to the content

• a light blue, dark blue, white and black colour scheme as seen on the homepage (www.tobiaskernwald.com) please use the exact same colours as seen on the homepage.

White being most predominant, 2 different blue used to highlight something, black for text on white background.

• One graphic would be cool, as long as it is blue. It could be waves-like graphic, or something like the white pattern in the background, in my case just in blue on white background > http://www.lumenquietharbor.org/., I do not mean exactly this graphic and not that crowded but a simple single graphic in blue as long as it fits the theme and feel of my poster

Top o f the poster

• (a )One short bold headline (TALK TITLE) with a sub-headline below it (hook)

• or (b) headline as question (…....?) and below sub-headline offering the solution (my talk ;-) of course)

• 3 benefits as on homepage, that I can adapt for each talk (bottom right of my start site “what are you looking for?” either blue on white, or as in the page white on blue...whatever looks better and fits the design). Not sure how that looks, and if to include it!

• the bottom of the poster will have “Where”-information “when”-information “ticket price” info

• contact at the very bottom...for more into or to purchase tickets (my website and email)

If you have any questions or need clarification please write me!

Requirements
Must have
• lot of white space
• less is more - simple design
• little text, little graphics- only used when necessary to greatest effect.
• light, friendly, modern feel
• blue-color scheme

```html
<!DOCTYPE html>
<html lang="en">
<head>
<meta charset="utf-8">
<title>Tobias Kernwald – Spiritual Speaker</title>
<link href="https://fonts.googleapis.com/css2?family=Arimo:wght@400&family=Noto+Sans:wght@400&display=swap" rel="stylesheet">
<style>
  :root {
    --frame-blue: #2a93c6;
    --brand-blue: #2a8fc4;
    --bullet-blue: #1f6fa0;
    --sky-tint: #e4f2fa;
    --ornament-tint: #eef3f7;
    --ink: #111111;
    --body-ink: #2b2b2b;
    --muted: #7a7a7a;
    --soft-grey: #9a9a9a;
    --paper: #ffffff;
  }
  * { margin: 0; padding: 0; box-sizing: border-box; }
  html, body { width: 849px; height: 1200px; overflow: hidden; background: var(--frame-blue); }
  .poster {
    position: relative;
    width: 849px;
    height: 1200px;
    background: var(--frame-blue);
    font-family: "Arimo", Arial, sans-serif;
  }
  .sheet {
    position: absolute;
    left: 10px; top: 10px;
    width: 829px; height: 1179px;
    border-radius: 20px;
    background: linear-gradient(180deg, var(--sky-tint) 0%, var(--paper) 30%, var(--paper) 100%);
    overflow: hidden;
  }
  .ornament {
    position: absolute;
    left: 170px; top: 360px;
    width: 490px; height: 460px;
    border-radius: 50%;
    background: radial-gradient(ellipse at center, var(--ornament-tint) 0%, rgba(238,243,247,0.5) 55%, rgba(255,255,255,0) 75%);
  }
  .brand-dot {
    position: absolute;
    left: 110px; top: 62px;
    width: 78px; height: 78px;
    border-radius: 50%;
    background: var(--brand-blue);
    opacity: 0.85;
  }
  .brand-name {
    position: absolute;
    left: 195px; top: 138px;
    font-size: 58px;
    line-height: 1;
    color: var(--brand-blue);
    white-space: nowrap;
  }
  .brand-role {
    position: absolute;
    left: 193px; top: 196px;
    font-size: 40px;
    line-height: 1;
    color: var(--muted);
    white-space: nowrap;
  }
  .headline {
    position: absolute;
    left: 0; top: 316px;
    width: 829px;
    text-align: center;
    font-family: "Arimo", Arial, sans-serif;
    font-weight: 400;
    font-size: 47px;
    line-height: 1;
    color: var(--brand-blue);
    text-shadow: 2px 2px 0 #1c1c1c;
    white-space: nowrap;
  }
  .subheadline {
    position: absolute;
    left: 0; top: 386px;
    width: 829px;
    text-align: center;
    font-size: 31px;
    line-height: 1;
    color: var(--soft-grey);
  }
  .benefits {
    position: absolute;
    left: 18px; top: 575px;
    list-style: none;
    font-family: "Noto Sans", Verdana, sans-serif;
    font-size: 17px;
    letter-spacing: 0.3px;
    color: var(--body-ink);
  }
  .benefits li {
    position: relative;
    padding-left: 30px;
    height: 45px;
    line-height: 20px;
    white-space: nowrap;
  }
  .benefits li::before {
    content: "";
    position: absolute;
    left: 0; top: 4px;
    width: 11px; height: 11px;
    background: var(--bullet-blue);
  }
  .event { position: absolute; left: 18px; color: var(--body-ink); }
  .event-label {
    font-size: 24px;
    font-weight: 400;
    line-height: 1;
    color: var(--brand-blue);
  }
  .event-detail { font-size: 15px; line-height: 22px; }
  .venue { top: 844px; }
  .venue .event-detail { margin-top: 8px; }
  .timing { top: 956px; }
  .timing .event-detail { margin-top: 9px; }
  .price-sign { font-size: 19px; }
  .contact-label {
    position: absolute;
    left: 18px; top: 1042px;
    font-size: 30px;
    line-height: 1;
    color: var(--ink);
  }
  .contact-url {
    position: absolute;
    left: 0; top: 1076px;
    width: 829px;
    text-align: center;
    font-family: "Noto Sans", Verdana, sans-serif;
    font-size: 48px;
    line-height: 1.1;
    color: var(--brand-blue);
    white-space: nowrap;
  }
</style>
</head>
<body>
<main class="poster">
  <section class="sheet">
    <div class="ornament" role="img" aria-label="Faint flourish ornament in pale blue-grey behind the headline"></div>

    <header>
      <span class="brand-dot" aria-hidden="true"></span>
      <div class="brand-name">TOBIAS KERNWALD</div>
      <div class="brand-role">SPIRITUAL SPEAKER</div>
    </header>

    <h1 class="headline">What is Spirituality for you?</h1>
    <p class="subheadline">We teach spitituality in its deepest.</p>

    <ul class="benefits">
      <li>Don't wonder what the world will bring to you, but choose what you will bring to the world</li>
      <li>You are a beautiful expression of life. You are worthwhile because&nbsp; you exist!</li>
      <li>Life isn't happening to you, it is happening for you!</li>
    </ul>

    <div class="event venue">
      <h2 class="event-label">Our next Seminar</h2>
      <p class="event-detail">123, Street XYZ Lane,<br>N500,Australia.12345</p>
    </div>

    <div class="event timing">
      <h2 class="event-label">On 30 Sep. 2010 9:00 am</h2>
      <p class="event-detail">Entry Fees:&nbsp; <span class="price-sign">£</span>30 Only</p>
    </div>

    <p class="contact-label">Contact:</p>
    <p class="contact-url">www.tobiaskernwald.com</p>
  </section>
</main>
</body>
</html>
```